Brindle Search Business Card for recruitment company

We are looking for a Business Card Design that incorporates our personal details and our busines name and logo. We are a specialized search consultancy that recruit Property and Construction professionals.
We would like a business card that stands out and is appealing to the Construction and Property industry as well.

Target Market(s)

people in the construction and property industry

Contact Information for Business Card

Business Name and logo

Font styles to use
Serif

Colors
0094D4
00A9DD
6FCCEA
C7EBF8
E9F6FB

Requirements
Must have
• Business name and logo as well as contact details
Should not have
• No photos of us please

```html
<!DOCTYPE html>
<html lang="en">
<head>
<meta charset="utf-8">
<title>Brindle Search — Business Card</title>
<link href="https://fonts.googleapis.com/css2?family=Lato:wght@300;400;900&display=swap" rel="stylesheet">
<style>
  :root {
    --backdrop: #2a2a2a;
    --teal: #053f55;
    --paper: #ffffff;
    --ink-light: #ffffff;
  }
  * { margin: 0; padding: 0; box-sizing: border-box; }
  html, body { width: 1200px; height: 1015px; overflow: hidden; }
  body {
    background: var(--backdrop);
    font-family: "Lato", sans-serif;
    display: flex;
    flex-direction: column;
    align-items: center;
    justify-content: center;
    gap: 60px;
  }
  .card {
    position: relative;
    width: 700px;
    height: 400px;
    background: var(--teal);
    overflow: hidden;
  }
  .card__art { position: absolute; inset: 0; width: 100%; height: 100%; }
  .wordmark {
    font-family: "Lato", sans-serif;
    font-weight: 300;
    letter-spacing: 0.08em;
    text-transform: uppercase;
    white-space: nowrap;
    display: flex;
    align-items: center;
    gap: 12px;
  }
  .wordmark__dot {
    width: 10px; height: 10px; border-radius: 50%;
    background: currentColor;
    flex: none;
  }
  .card--front .wordmark {
    position: absolute; left: 50%; top: 50%;
    transform: translate(-50%, -50%);
    color: var(--ink-light);
    font-size: 42px;
  }
  .card--back .wordmark {
    position: absolute; right: 40px; top: 168px;
    color: var(--teal);
    font-size: 25px;
  }
  .person {
    position: absolute; left: 60px; top: 110px;
    color: var(--ink-light);
  }
  .person__name { font-weight: 900; font-size: 19px; letter-spacing: 0.03em; text-transform: uppercase; }
  .person__role { font-weight: 400; font-size: 16px; margin-top: 2px; }
  .contact {
    position: absolute; left: 60px; top: 232px;
    color: var(--ink-light);
    font-size: 16px;
    line-height: 1.35;
  }
  .contact__address { margin-bottom: 14px; }
  .contact__list { list-style: none; }
  .contact__item { display: flex; align-items: center; gap: 10px; }
  .contact__icon { width: 15px; height: 15px; flex: none; }
</style>
</head>
<body>

  <section class="card card--front" aria-label="Card front">
    <div class="wordmark"><span class="wordmark__dot"></span>Brindle Search</div>
  </section>

  <section class="card card--back" aria-label="Card back">
    <svg class="card__art" viewBox="0 0 700 400" aria-hidden="true">
      <circle cx="575" cy="160" r="262" fill="var(--paper)"/>
      <circle cx="586" cy="156" r="255" fill="var(--teal)"/>
      <circle cx="592" cy="153" r="250" fill="var(--paper)"/>
    </svg>

    <div class="wordmark"><span class="wordmark__dot"></span>Brindle Search</div>

    <div class="person">
      <p class="person__name">Marcus Hale</p>
      <p class="person__role">Managing Director</p>
    </div>

    <div class="contact">
      <p class="contact__address">17, Harbour Row<br>Eastbridge, 30418</p>
      <ul class="contact__list">
        <li class="contact__item">
          <svg class="contact__icon" viewBox="0 0 24 24"><path fill="#fff" d="M6.6 10.8a15.1 15.1 0 0 0 6.6 6.6l2.2-2.2a1 1 0 0 1 1-.25 11.4 11.4 0 0 0 3.6.57 1 1 0 0 1 1 1V20a1 1 0 0 1-1 1A17 17 0 0 1 3 4a1 1 0 0 1 1-1h3.5a1 1 0 0 1 1 1c0 1.25.2 2.45.57 3.57a1 1 0 0 1-.25 1z"/></svg>
          044-555 010 234
        </li>
        <li class="contact__item">
          <svg class="contact__icon" viewBox="0 0 24 24"><rect x="2" y="5" width="20" height="14" fill="#fff"/><path d="M2 5l10 8 10-8" fill="none" stroke="var(--teal)" stroke-width="2"/></svg>
          hello@brindlesearch.com
        </li>
        <li class="contact__item">
          <svg class="contact__icon" viewBox="0 0 24 24" fill="none" stroke="#fff" stroke-width="2"><circle cx="12" cy="12" r="10"/><ellipse cx="12" cy="12" rx="4.5" ry="10"/><path d="M2 12h20M4 7h16M4 17h16"/></svg>
          www.brindlesearch.com
        </li>
      </ul>
    </div>
  </section>

</body>
</html>
```